a save the date design that can also be used for an invitation

We want to use the name 'Jo'
Also a subtle nod to the Fernbridge Rovers logo
Also very small illustrations so indicate food (a burger or pizza), drinks (cocktail) and dancing (musical notes).
Also a small scroll.

Once we see the detail we can think how to space them so I can use them on paperless post.

The style needs to be modern, suitable for a 12 year old boy and colours only blues and white.

```html
<!DOCTYPE html>
<html lang="en">
<head>
<meta charset="utf-8">
<title>Jo – Save the Date</title>
<link href="https://fonts.googleapis.com/css2?family=Jost:wght@500;600&family=Montserrat:wght@500&display=swap" rel="stylesheet">
<style>
  :root {
    --navy: #021d57;
    --shield-line: #1c3f86;
    --accent-blue: #3a7bd5;
    --white: #ffffff;
    --page: #ffffff;
  }
  * { margin: 0; padding: 0; box-sizing: border-box; }
  html, body { width: 1200px; height: 1200px; overflow: hidden; background: var(--page); }
  .canvas { position: relative; width: 1200px; height: 1200px; }
  .invite-card {
    position: absolute; left: 348px; top: 63px; width: 505px; height: 630px;
    background: var(--navy);
    box-shadow: 10px 10px 8px rgba(0,0,0,0.18);
  }
  .invite-banner {
    position: absolute; left: 0; top: 811px; width: 1200px; height: 389px;
    background: var(--navy);
  }
  .crest { position: absolute; display: block; }
  .invite-card .crest { left: 72px; top: 100px; width: 360px; height: 420px; }
  .invite-banner .crest { left: 496px; top: 80px; width: 209px; height: 244px; }
  .crest-name { font-family: "Montserrat", sans-serif; font-weight: 500; fill: var(--white); }
  .crest-club { font-family: "Jost", sans-serif; font-weight: 600; fill: var(--shield-line); letter-spacing: 2px; }
  .crest-tagline { font-family: "Jost", sans-serif; font-weight: 600; fill: var(--white); letter-spacing: 1.5px; }
  .shield { fill: none; stroke: var(--shield-line); stroke-width: 4; }
  .shield-gap { fill: var(--navy); }
  .rule { stroke: var(--accent-blue); stroke-width: 2; }
  .icon { fill: none; stroke: var(--white); stroke-width: 2; stroke-linecap: round; stroke-linejoin: round; }
  .icon-fill { fill: var(--white); stroke: none; }
</style>
</head>
<body>
<main class="canvas">
  <svg width="0" height="0" style="position:absolute">
    <defs>
      <symbol id="crest-mark" viewBox="0 0 360 420">
        <path class="shield" d="M13 100 Q180 66 347 100 L347 200 Q335 320 180 400 Q25 320 13 200 Z"/>
        <path class="shield" d="M27 112 Q180 80 333 112 L333 200 Q322 308 180 385 Q38 308 27 200 Z"/>
        <rect class="shield-gap" x="0" y="280" width="360" height="66"/>
        <text class="crest-club" x="180" y="66" text-anchor="middle" font-size="16">FERNBRIDGE ROVERS</text>
        <text class="crest-name" x="180" y="250" text-anchor="middle" font-size="178" letter-spacing="6">JO</text>
        <line class="rule" x1="67" y1="291" x2="89" y2="291"/>
        <line class="rule" x1="273" y1="291" x2="295" y2="291"/>
        <text class="crest-tagline" x="181" y="298" text-anchor="middle" font-size="19" textLength="168" lengthAdjust="spacingAndGlyphs">SAVE THE DATE</text>
        <g class="icon-row">
          <g class="icon burger" transform="translate(82 326)">
            <path d="M-13 -3 a13 11 0 0 1 26 0 Z"/>
            <path d="M-14 2 h28"/>
            <path d="M-14 7 q3.5 -3 7 0 q3.5 3 7 0 q3.5 -3 7 0 q3.5 3 7 0"/>
            <path d="M-13 11 h26 v1 a3 3 0 0 1 -3 3 h-20 a3 3 0 0 1 -3 -3 Z"/>
          </g>
          <g class="icon pizza" transform="translate(131 328)">
            <path d="M-14 11 L9 -12 L13 13 Z"/>
            <path d="M7 -14 q6 12 8 28"/>
            <circle cx="1" cy="5" r="2"/>
            <circle cx="7" cy="8" r="1.6"/>
          </g>
          <g class="icon cocktail" transform="translate(180 328)">
            <path d="M-13 -10 h26 l-13 14 Z"/>
            <path d="M0 4 v11 M-7 15 h14"/>
            <path d="M4 -10 l7 -7"/>
            <circle cx="-5" cy="-14" r="3"/>
          </g>
          <g class="icon notes" transform="translate(229 328)">
            <path d="M-6 10 v-21 l14 -4 v20"/>
            <ellipse class="icon-fill" cx="-9" cy="10" rx="3.5" ry="2.6"/>
            <ellipse class="icon-fill" cx="5" cy="5" rx="3.5" ry="2.6"/>
          </g>
          <g class="icon scroll" transform="translate(278 326)">
            <path d="M-14 -8 h26 a4 4 0 0 1 0 8 h-26 a4 4 0 0 1 0 -8 Z"/>
            <path d="M-10 0 v6 a4 4 0 0 0 4 4 h18"/>
            <path d="M8 0 l-3 12 l4 -3 l3 4 l1 -13"/>
          </g>
        </g>
      </symbol>
    </defs>
  </svg>

  <section class="invite-card" aria-label="Save the date card">
    <svg class="crest" viewBox="0 0 360 420" role="img" aria-label="Jo, save the date"><use href="#crest-mark"/></svg>
  </section>

  <section class="invite-banner" aria-label="Save the date banner">
    <svg class="crest" viewBox="0 0 360 420" role="img" aria-label="Jo, save the date"><use href="#crest-mark"/></svg>
  </section>
</main>
</body>
</html>
```